Website redesign www.brindlecovepc.com law firm site

Need to redesign the website that I currently have to look more modern and professional. Would also like to be able to make updates and post without having a huge hassle. See current www.brindlecovepc.com. I just think that it looks very immature and it's very templated there's no ability for me to make posts or Add links or anything like that

Target Market(s)

California people looking for a powerhouse attorney in

Industry/Entity Type

Legal

Number of Pages Required

3 page

Font styles to use
Serif
Sans Serif

Colors
ec1f27
000000
ffffff

Requirements
Must have
• Must be mobile friendly. Must look professional and have ability to post links to other websites. Must have ability to post blogs or articles. Would like to be able to read my Quindral account and also have the ability to upload forms for people to download
Nice to have
• Simple design easy to use and not cluttered with too much text

```html
<!DOCTYPE html>
<html lang="en">
<head>
<meta charset="utf-8">
<title>Brindle Cove Law, P.C. — Chico California Attorney</title>
<link href="https://fonts.googleapis.com/css2?family=Noto+Serif:wght@400;700&family=Open+Sans:wght@400;600&display=swap" rel="stylesheet">
<style>
:root{
  --red:#ec1f27;
  --ink:#1a1a1a;
  --text:#555;
  --muted:#999;
  --nav:#3b3b3b;
  --light:#f3f3f3;
  --line:#e2e2e2;
  --navy:#1b2941;
  --navy-deep:#142036;
  --white:#fff;
}
*{box-sizing:border-box;margin:0;padding:0}
html,body{width:1200px;height:3396px;overflow:hidden}
body{font-family:"Open Sans",Arial,sans-serif;color:var(--text);background:var(--white);position:relative;font-size:13px}
.serif{font-family:"Noto Serif",Georgia,serif}
section,header,nav,footer{position:absolute;left:0;width:1200px}
.abs{position:absolute}

/* header */
.topbar{top:0;height:95px;background:var(--white)}
.contact-mini{left:154px;top:26px;display:flex;gap:12px;align-items:center}
.contact-mini .ring{width:26px;height:26px;border:2px solid var(--red);border-radius:50%;display:flex;align-items:center;justify-content:center}
.contact-mini b{display:block;font-weight:400;font-size:17px;color:#333}
.contact-mini small{display:block;font-size:11px;color:#777}
.brand{left:0;width:1200px;top:14px;text-align:center;color:var(--red);font-family:"Noto Serif",Georgia,serif;font-variant:small-caps;line-height:1}
.brand .name{font-size:36px;letter-spacing:.5px}
.brand .pc{font-size:16px;margin-top:4px}
.btn-consult{left:869px;top:29px;width:172px;height:32px;border:1px solid #ddd;border-radius:16px;display:flex;align-items:center;justify-content:center;gap:8px;font-size:12px;color:#555}

.mainnav{top:95px;height:36px;background:var(--nav)}
.mainnav a{position:absolute;top:0;height:36px;line-height:36px;color:var(--white);font-family:"Noto Serif",Georgia,serif;font-size:14px;text-decoration:none;letter-spacing:.3px}
.mainnav .active{background:var(--red);padding:0 16px}
.dropdown{left:421px;top:131px;width:154px;background:var(--white);z-index:5;box-shadow:0 2px 6px rgba(0,0,0,.08);padding:4px 0}
.dropdown li{list-style:none;font-family:"Noto Serif",Georgia,serif;font-size:11px;color:#777;height:28px;line-height:28px;padding-left:14px}
.dropdown li::before{content:"› ";}
.dropdown li.on{background:var(--red);color:var(--white)}

.hero{top:131px;height:351px;background:linear-gradient(180deg,#e3e8ed 0%,#f4f6f8 45%,#dfe4ea 100%)}
.hero-art{left:374px;top:9px;width:464px;height:324px;border-radius:8px;background:radial-gradient(ellipse at center,rgba(120,20,20,.55) 0%,rgba(150,60,40,.25) 45%,rgba(230,235,240,0) 72%)}
.circle-arrow{width:34px;height:34px;border:1px solid #aaa;border-radius:50%;display:flex;align-items:center;justify-content:center;background:rgba(255,255,255,.5)}

/* about */
.about{top:482px;height:424px;background:var(--light)}
.about .redblock{left:154px;top:57px;width:62px;height:62px;background:var(--red)}
.about .portrait{left:172px;top:73px;width:285px;height:294px;background:linear-gradient(160deg,#d9c3b2,#b48a6f 55%,#8a6a55);border:6px solid var(--white)}
.about .kicker{left:537px;top:60px;font-size:14px;color:#555}
.about h1{position:absolute;left:537px;top:84px;font-family:"Noto Serif",Georgia,serif;font-size:22px;color:var(--ink);font-weight:700}
.about p{position:absolute;left:537px;width:510px;font-size:12.5px;line-height:1.6;color:#777}
.btn-outline{position:absolute;border:1px solid #999;border-radius:18px;font-size:12px;color:#555;display:flex;align-items:center;justify-content:center;background:var(--white)}

/* section titles */
.section-title{left:0;width:1200px;text-align:center}
.section-title h2{font-family:"Noto Serif",Georgia,serif;font-size:24px;color:var(--ink);font-weight:700;margin-top:10px}
.emblem{display:block;margin:0 auto}

/* practice */
.practice{top:906px;height:674px;background:var(--white)}
.card{position:absolute;width:281px;height:204px;border:1px solid var(--line);background:var(--white);text-align:center;padding-top:30px}
.card h3{font-family:"Noto Serif",Georgia,serif;font-weight:400;font-size:17px;color:#333;margin:8px 0 12px}
.card p{font-size:11.5px;line-height:1.5;color:#888;padding:0 30px}
.card svg{display:block;margin:0 auto}
.card.feature{background:linear-gradient(180deg,#c2323a 0%,#b11f28 60%,#a11820 100%);border-color:#b11f28;box-shadow:0 6px 12px rgba(0,0,0,.2)}
.card.feature h3,.card.feature p{color:var(--white)}

/* reviews */
.reviews{top:1580px;height:363px;background:var(--light)}
.reviews .avatar{left:242px;top:145px;width:125px;height:125px;border-radius:50%;border:5px solid var(--white);background:linear-gradient(160deg,#e0c2a4,#9d6f4f 60%,#5a4a44);box-shadow:0 1px 4px rgba(0,0,0,.12)}
.reviews .quote-mark{left:392px;top:144px;font-family:"Noto Serif",Georgia,serif;font-size:44px;color:#333;line-height:1}
.reviews blockquote{position:absolute;left:435px;top:157px;width:530px;font-size:12.5px;line-height:1.65;color:#777}
.reviews .by{left:435px;top:272px;font-size:13px;color:#444}
.reviews .org{left:435px;top:293px;font-size:11.5px;color:#888}

/* blog */
.blog{top:1943px;height:570px;background:var(--white)}
.blog .lead-img{left:156px;top:158px;width:399px;height:204px;background:linear-gradient(120deg,#3b2414 0%,#8b5a2b 45%,#c8955a 65%,#2a1a10 100%)}
.date{position:absolute;width:45px;background:var(--red);color:var(--white);text-align:center;font-family:"Noto Serif",Georgia,serif}
.date b{display:block;font-size:20px;line-height:30px}
.date span{display:block;font-size:10px;line-height:15px;background:#b9b9b9}
.blog h4{font-family:"Noto Serif",Georgia,serif;font-weight:400;color:#333}
.meta{font-size:10px;color:#aaa}
.post{position:absolute;left:593px;width:451px;height:79px;background:var(--light)}
.post.hot{background:#faf2f2}
.post h4{position:absolute;left:64px;top:10px;width:370px;font-size:13.5px;line-height:1.3}
.post.hot h4{color:var(--red)}
.post .meta{position:absolute;left:64px;top:55px}
.link-more{font-size:11.5px;color:#444}
.link-red{font-size:11.5px;color:var(--red)}

/* ratings */
.ratings{top:2513px;height:287px;background:var(--light)}
.badge-seal{left:197px;top:144px;width:77px;height:77px;border-radius:50%;border:3px solid #444;background:#e8e8e8}
.badge-bar{height:40px;background:#d5d8dd}
.badge-shield{left:894px;top:136px;width:90px;height:96px;border-radius:50%;background:var(--white);border:5px solid #1d3b6e}
.divider-v{width:1px;height:60px;background:#ccc;top:152px}

/* footer */
.site-footer{top:2800px;height:517px;background:linear-gradient(180deg,var(--navy) 0%,#1a2740 100%)}
.ficon{width:42px;height:42px;border-radius:50%;background:var(--white);display:flex;align-items:center;justify-content:center}
.finfo{color:var(--white);font-size:13.5px;text-align:center;line-height:1.5}
.site-footer h5{position:absolute;font-family:"Noto Serif",Georgia,serif;font-weight:400;font-size:17px;color:var(--white)}
.field{position:absolute;border:1px solid #c9ced8;height:32px;color:var(--white);font-size:11px;padding:8px 12px;background:transparent}
.send{left:154px;top:440px;width:91px;height:32px;border-radius:16px;background:var(--white);color:#333;font-size:12px;display:flex;align-items:center;justify-content:center;gap:8px}
.sitelinks{left:840px;top:278px;list-style:none}
.sitelinks li{font-size:11.5px;color:var(--white);line-height:24px}
.sitelinks li::before{content:"› "}
.sitelinks li.on{color:var(--red)}
.social{width:24px;height:24px;border:1px solid #aab;border-radius:50%;top:433px}
.bottombar{top:3317px;height:79px;background:var(--navy-deep);color:#d8dbe2;font-size:11px}
</style>
</head>
<body>

<header class="topbar">
  <div class="abs contact-mini">
    <div class="ring"><svg width="12" height="12" viewBox="0 0 24 24"><path d="M6.6 10.8a15 15 0 0 0 6.6 6.6l2.2-2.2c.3-.3.7-.4 1-.2 1.1.4 2.3.6 3.6.6.6 0 1 .4 1 1V20c0 .6-.4 1-1 1A17 17 0 0 1 3 4c0-.6.4-1 1-1h3.5c.6 0 1 .4 1 1 0 1.3.2 2.5.6 3.6.1.3 0 .7-.2 1z" fill="#ec1f27"/></svg></div>
    <div><b>(530) 555-0148</b><small>marian@brindlecovegroup.com</small></div>
  </div>
  <div class="abs brand"><div class="name">Brindle Cove Law</div><div class="pc">P.C.</div></div>
  <div class="abs btn-consult">
    <svg width="14" height="12" viewBox="0 0 14 12"><path d="M1 1h9v6H4l-3 3z" fill="#ec1f27"/><path d="M11 4h2v6l-2-2H6V8" fill="none" stroke="#ec1f27"/></svg>
    Free Consulations
  </div>
</header>

<nav class="mainnav">
  <a style="left:154px">Home</a>
  <a style="left:254px">Attorney Profile</a>
  <a class="active" style="left:421px;width:154px">Practice Areas ⌄</a>
  <a style="left:629px">Client Reviews</a>
  <a style="left:801px">Links&amp;Forms</a>
  <a style="left:960px">Contact Us</a>
</nav>
<ul class="abs dropdown">
  <li>Business Law</li>
  <li>Real Estate Law</li>
  <li class="on">Bankruptcy</li>
  <li>Family Law</li>
  <li>Criminal Law</li>
  <li>Civil Litigation</li>
</ul>

<section class="hero">
  <div class="abs hero-art" role="img" aria-label="Word cloud of legal terms centred on the words criminal law legal"></div>
  <div class="abs circle-arrow" style="left:40px;top:157px"><svg width="10" height="10" viewBox="0 0 10 10"><path d="M7 1 3 5l4 4" fill="none" stroke="#666" stroke-width="1.5"/></svg></div>
  <div class="abs circle-arrow" style="left:1129px;top:157px"><svg width="10" height="10" viewBox="0 0 10 10"><path d="M3 1l4 4-4 4" fill="none" stroke="#666" stroke-width="1.5"/></svg></div>
</section>

<section class="about">
  <div class="abs redblock"></div>
  <div class="abs portrait" role="img" aria-label="Portrait photo of the attorney"></div>
  <div class="abs kicker">Brindle Cove Law, P.C.</div>
  <h1>Chico California Attorney</h1>
  <p style="top:128px">Find the big firm style legal counsel you can work with in your hometown region at Brindle Cove Law P.C., in Chico, CA. Attorney Marian L. Hale, Esq., offers a boutique law firm opportunity for clients who want to enjoy all the advantages of her broad legal experience and education. She works closely with clients, and has the knowledge of many areas of law to apply to your situation.</p>
  <p style="top:234px">This is very helpful when it is necessary to incorporate those different areas of law practice into creating a winning argument for your unique case.</p>
  <div class="btn-outline" style="left:537px;top:326px;width:145px;height:32px">Discover About Us</div>
</section>

<section class="practice">
  <div class="abs section-title" style="top:44px">
    <svg class="emblem" width="40" height="26" viewBox="0 0 40 26"><path d="M0 13h12M28 13h12" stroke="#ec1f27"/><path d="M20 3v16M13 6h14M13 6l-3 7h6zM27 6l-3 7h6zM16 20h8" stroke="#ec1f27" fill="none" stroke-width="1.5"/></svg>
    <h2>Practice areas</h2>
  </div>
  <div class="card" style="left:156px;top:133px">
    <svg width="40" height="32" viewBox="0 0 40 32"><rect x="2" y="8" width="36" height="22" rx="2" fill="#777"/><rect x="14" y="2" width="12" height="8" rx="2" fill="none" stroke="#777" stroke-width="3"/></svg>
    <h3>Business Law</h3>
    <p>Small and medium sized businesses have many of the same legal issues that affect large businesse.</p>
  </div>
  <div class="card feature" style="left:460px;top:133px" role="img" aria-label="Red tinted photo of a house behind the Real Estate Law card">
    <svg width="40" height="32" viewBox="0 0 40 32"><path d="M4 16 20 3l16 13" fill="none" stroke="#fff" stroke-width="3"/><path d="M9 14v16h22V14" fill="#fff"/><circle cx="20" cy="21" r="5" fill="#b11f28"/></svg>
    <h3>Real Estate Law</h3>
    <p>At Brindle Cove Law P.C., we help Californians who need legal advice and representation for Real Estate...</p>
  </div>
  <div class="card" style="left:763px;top:133px">
    <svg width="40" height="32" viewBox="0 0 40 32"><rect x="6" y="4" width="16" height="9" transform="rotate(-30 14 8)" fill="#777"/><path d="M16 12 30 28" stroke="#777" stroke-width="4"/></svg>
    <h3>Bankruptcy</h3>
    <p>If your finances are dwindling to the point where you can no longer pay your bills, and you are getting...</p>
  </div>
  <div class="card" style="left:156px;top:364px">
    <svg width="40" height="32" viewBox="0 0 40 32"><circle cx="12" cy="8" r="5" fill="#777"/><circle cx="28" cy="8" r="5" fill="#777"/><circle cx="20" cy="15" r="5" fill="#777"/><path d="M3 22c0-6 18-6 18 0zM19 22c0-6 18-6 18 0zM10 30c0-7 20-7 20 0z" fill="#777"/></svg>
    <h3>Family Law</h3>
    <p>Family Law is one area of legal concern that brings many people in to see our experienced...</p>
  </div>
  <div class="card" style="left:460px;top:364px">
    <svg width="40" height="32" viewBox="0 0 40 32"><circle cx="11" cy="18" r="8" fill="none" stroke="#777" stroke-width="3"/><circle cx="29" cy="14" r="8" fill="none" stroke="#777" stroke-width="3"/><path d="M17 12h6" stroke="#777" stroke-width="2"/></svg>
    <h3>Criminal Law</h3>
    <p>Chico Criminal Law Attorney If you were charged with a criminal offense, or if you are under...</p>
  </div>
  <div class="card" style="left:763px;top:364px">
    <svg width="40" height="32" viewBox="0 0 40 32"><rect x="10" y="2" width="16" height="9" transform="rotate(35 18 6)" fill="#777"/><path d="M16 10 6 24" stroke="#777" stroke-width="4"/><rect x="4" y="26" width="32" height="5" fill="#777"/></svg>
    <h3>Civil Litigation</h3>
    <p>Civil Litigation is a vast legal category than can include everything from personal injury cases...</p>
  </div>
  <div class="btn-outline" style="left:528px;top:595px;width:147px;height:36px">View All Practices</div>
</section>

<section class="reviews">
  <div class="abs section-title" style="top:68px">
    <svg class="emblem" width="40" height="26" viewBox="0 0 40 26"><path d="M0 13h12M28 13h12" stroke="#ec1f27"/><path d="M20 3v16M13 6h14M13 6l-3 7h6zM27 6l-3 7h6zM16 20h8" stroke="#ec1f27" fill="none" stroke-width="1.5"/></svg>
    <h2>Client Reviews</h2>
  </div>
  <div class="abs circle-arrow" style="left:155px;top:196px"><svg width="10" height="10" viewBox="0 0 10 10"><path d="M7 1 3 5l4 4" fill="none" stroke="#666" stroke-width="1.5"/></svg></div>
  <div class="abs circle-arrow" style="left:1009px;top:196px;border-color:var(--red)"><svg width="10" height="10" viewBox="0 0 10 10"><path d="M3 1l4 4-4 4" fill="none" stroke="#ec1f27" stroke-width="1.5"/></svg></div>
  <div class="abs avatar" role="img" aria-label="Photo of the reviewing client"></div>
  <div class="abs quote-mark">“</div>
  <blockquote>Brindle Cove Law is our go to source for professional and sound legal advice. Brindle Cove Law has become a vital component to the success of our business as well as the businesses of the clients we have referred to Brindle Cove Law professional and sound legal advice. Brindle Cove Law has become a vital.</blockquote>
  <div class="abs by">— &nbsp;A Vital Component</div>
  <div class="abs org">Ridgeline Accounting Group</div>
</section>

<section class="blog">
  <div class="abs section-title" style="top:66px">
    <svg class="emblem" width="40" height="26" viewBox="0 0 40 26"><path d="M0 13h12M28 13h12" stroke="#ec1f27"/><path d="M20 3v16M13 6h14M13 6l-3 7h6zM27 6l-3 7h6zM16 20h8" stroke="#ec1f27" fill="none" stroke-width="1.5"/></svg>
    <h2>Our Latest Blog</h2>
  </div>
  <div class="abs lead-img" role="img" aria-label="Photo of a gavel and brass scales on law books"></div>
  <div class="date" style="left:156px;top:158px"><b>25</b><span>Jun</span></div>
  <h4 class="abs" style="left:156px;top:380px;font-size:15px">Criminal liability of an enterprise</h4>
  <div class="abs meta" style="left:156px;top:414px">Posted By: Jon Ellis &nbsp;&nbsp; View:65 &nbsp;&nbsp; Comment:174</div>
  <p class="abs" style="left:156px;top:436px;width:380px;font-size:11px;line-height:1.5;color:#888">Lorem Ipsum is simply dummy text of the printing and typesetting Lorem Ipsum has been the industry's standard dummy text ever since. Lorem Ipsum is simply dummy.</p>
  <div class="abs link-red" style="left:156px;top:500px">» Read More</div>

  <div class="post" style="top:158px"><div class="date" style="left:0;top:12px"><b>26</b><span>Aug</span></div><h4>Useless laws weaken the necessary laws. reach if you just keep climbing</h4><div class="meta">Posted By: Jon Ellis &nbsp;&nbsp; View:65 &nbsp;&nbsp; Comment:174</div></div>
  <div class="post hot" style="top:271px"><div class="date" style="left:0;top:12px"><b>27</b><span>Aug</span></div><h4>Every mountain top is within reach if you just keep climbing</h4><div class="meta">Posted By: Jon Ellis &nbsp;&nbsp; View:65 &nbsp;&nbsp; Comment:174</div></div>
  <div class="post" style="top:384px"><div class="date" style="left:0;top:12px"><b>28</b><span>Aug</span></div><h4>Useless laws weaken the necessary laws. reach if you just keep climbing</h4><div class="meta">Posted By: Jon Ellis &nbsp;&nbsp; View:65 &nbsp;&nbsp; Comment:174</div></div>
  <div class="abs link-more" style="left:598px;top:500px">» More Blog</div>
</section>

<section class="ratings">
  <div class="abs section-title" style="top:68px">
    <svg class="emblem" width="40" height="26" viewBox="0 0 40 26"><path d="M0 13h12M28 13h12" stroke="#ec1f27"/><path d="M20 3v16M13 6h14M13 6l-3 7h6zM27 6l-3 7h6zM16 20h8" stroke="#ec1f27" fill="none" stroke-width="1.5"/></svg>
    <h2>Ratings and Reviews</h2>
  </div>
  <div class="abs badge-seal" role="img" aria-label="Bar association seal badge"></div>
  <div class="abs divider-v" style="left:300px"></div>
  <div class="abs badge-bar" style="left:335px;top:163px;width:213px" role="img" aria-label="Lawyer directory listing badge"></div>
  <div class="abs divider-v" style="left:580px"></div>
  <div class="abs badge-bar" style="left:611px;top:163px;width:174px;background:#cfcfcf" role="img" aria-label="Partner property firm badge"></div>
  <div class="abs divider-v" style="left:850px"></div>
  <div class="abs badge-shield" role="img" aria-label="Attorney rating award badge"></div>
</section>

<footer class="site-footer">
  <div class="abs ficon" style="left:271px;top:54px"><svg width="16" height="16" viewBox="0 0 24 24"><path d="M6.6 10.8a15 15 0 0 0 6.6 6.6l2.2-2.2c.3-.3.7-.4 1-.2 1.1.4 2.3.6 3.6.6.6 0 1 .4 1 1V20c0 .6-.4 1-1 1A17 17 0 0 1 3 4c0-.6.4-1 1-1h3.5c.6 0 1 .4 1 1 0 1.3.2 2.5.6 3.6.1.3 0 .7-.2 1z" fill="#ec1f27"/></svg></div>
  <div class="abs ficon" style="left:563px;top:54px"><svg width="16" height="16" viewBox="0 0 16 16"><path d="M15 1 1 7l6 2 2 6z" fill="#ec1f27"/></svg></div>
  <div class="abs ficon" style="left:830px;top:54px"><svg width="16" height="16" viewBox="0 0 16 16"><path d="M8 1a5 5 0 0 0-5 5c0 4 5 9 5 9s5-5 5-9a5 5 0 0 0-5-5z" fill="#ec1f27"/><circle cx="8" cy="6" r="2" fill="#fff"/></svg></div>
  <div class="abs finfo" style="left:192px;top:110px;width:242px">(530) 555-0148</div>
  <div class="abs finfo" style="left:464px;top:110px;width:240px">418 W 5th Street<br>Suite 210, Chico, CA 95928</div>
  <div class="abs finfo" style="left:731px;top:110px;width:240px">Map and Directions</div>
  <div class="abs" style="left:154px;top:193px;width:890px;height:1px;background:#3a4862"></div>

  <h5 style="left:154px;top:244px">Request Your Free Consulation</h5>
  <div class="field" style="left:154px;top:290px;width:256px">Name</div>
  <div class="field" style="left:154px;top:338px;width:256px">Email</div>
  <div class="field" style="left:154px;top:383px;width:256px">Phone Number</div>
  <div class="field" style="left:428px;top:290px;width:278px;height:123px">Describe your case</div>
  <div class="abs send">Send <svg width="12" height="12" viewBox="0 0 16 16"><path d="M15 1 1 7l6 2 2 6z" fill="#333"/></svg></div>

  <h5 style="left:840px;top:244px">Site Links</h5>
  <ul class="abs sitelinks">
    <li>Home</li><li class="on">Attorney Profile</li><li>Practice Areas</li><li>Client Reviews</li><li>Contact Us</li>
  </ul>
  <div class="abs social" style="left:844px"></div>
  <div class="abs social" style="left:880px"></div>
  <div class="abs social" style="left:916px"></div>
</footer>

<div class="abs bottombar" style="left:0;width:1200px">
  <span class="abs" style="left:154px;top:30px">© 2016 Brindle Cove Law, P.C. All Rights Reserved</span>
  <span class="abs" style="left:828px;top:30px">Disclaimer &nbsp; / &nbsp; Site Map &nbsp; / &nbsp; Sign In</span>
</div>

</body>
</html>
```